Visitenkarten-Design für Psycho-Kinesiologie Praxis
Zielgruppe
praxis für Psycho-Kinesiologie - Systematische Familienaufstellungen. Einzelsitzungen Gruppentherapie
Ich suche ein Design was auf der einen Seite auffällt, aus dem Rahmen fällt und trotzdem seriös wirkt und Vertrauen schafft.
Die Anhänge sind nur meine Entwürfe also keine fixen Vorgaben
Aufgabenstellung
Eine Seite soll auffallen und Kreativ gestaltet sein
Es gibt ein Template aber die Farben sind noch nicht definiert.
https://www.vorlagenhafen.com/de/demo/48352.html
Es gibt ein Logo (Systemanalytiker) da sind die Farben auch nicht fix Definiert. Gerne sehe ich verschiedene Farbkombinationen
Foto: besseres folgt in kürze
Lumen Harbor Circle: Kann auf einer Seite drauf sein, wenn genug Platz,

```html
<!DOCTYPE html>
<html lang="de">
<head>
<meta charset="utf-8">
<title>Seelenraum – Visitenkarten Farbvarianten</title>
<link rel="stylesheet" href="https://fonts.googleapis.com/css2?family=Jost:wght@300;400;600&display=swap">
<style>
  :root {
    --sheet: #ffffff;
    --card: #2a2d30;
    --band: #45494c;
    --band-grey: #9b9b9b;
    --ink: #ffffff;
    --ink-soft: #e4e4e4;
    --ink-dark: #2a2d30;
    --red: #d3122a;
    --gold: #c9a227;
    --grey: #8d8f91;
    --photo-a: #9a9a9a;
    --photo-b: #4a4a4a;
  }
  * { margin: 0; padding: 0; box-sizing: border-box; }
  html, body { width: 857px; height: 1200px; overflow: hidden; background: var(--sheet); }
  body { position: relative; font-family: "Jost", "Futura", sans-serif; color: var(--ink); }

  .card {
    position: absolute; width: 229px; height: 147px;
    background: var(--card); overflow: hidden;
    box-shadow: 1px 2px 4px rgba(0,0,0,.28);
  }
  .col-front { left: 185px; }
  .col-back { left: 437px; }

  .motto {
    position: absolute; left: 0; right: 0; bottom: 0; height: 12px;
    background: var(--band); border-top: 1.5px solid var(--ink);
    font-size: 7px; letter-spacing: 1.6px; line-height: 10px; text-align: center;
    color: var(--ink);
  }
  .accent-gold .motto { border-top-color: var(--gold); background: var(--card); }
  .tone-grey .motto { background: var(--band-grey); border-top-color: var(--band-grey); color: var(--ink-dark); }

  .brand { position: absolute; display: flex; align-items: center; gap: 4px; white-space: nowrap; }
  .brand-dot { border-radius: 50%; background: var(--red); flex: none; }
  .dot-gold .brand-dot { background: var(--gold); }
  .dot-grey .brand-dot { background: var(--grey); }
  .brand-name { font-weight: 300; color: var(--ink); line-height: 1; }

  .brand-lg { left: 0; right: 0; justify-content: center; }
  .brand-lg .brand-dot { width: 11px; height: 11px; }
  .brand-lg .brand-name { font-size: 25px; }
  .brand-sm .brand-dot { width: 6px; height: 6px; }
  .brand-sm .brand-name { font-size: 14px; }

  .services-line {
    position: absolute; left: 0; right: 0; top: 102px;
    font-size: 5.8px; line-height: 8.2px; text-align: center; color: var(--ink-soft);
  }
  .front-name {
    position: absolute; right: 36px; top: 99px;
    font-size: 12px; font-weight: 300; color: var(--ink-soft);
  }

  .person { position: absolute; left: 7px; line-height: 1.15; }
  .person-name { font-size: 8px; font-weight: 600; }
  .person-role { font-size: 6.5px; font-weight: 300; color: var(--ink-soft); }

  .contacts { position: absolute; left: 6px; font-size: 5.2px; line-height: 7px; color: var(--ink-soft); list-style: none; }
  .contacts li { display: flex; gap: 3px; }
  .contacts svg { width: 5px; height: 5px; flex: none; margin-top: 1px; fill: var(--ink); }
  .contacts .indent { padding-left: 8px; }
  .contacts .gap { margin-top: 2px; }

  .portrait {
    position: absolute; left: 114px; top: 0; width: 115px; height: 134px;
    background: linear-gradient(160deg, var(--photo-a), var(--photo-b));
  }

  .partner { position: absolute; display: flex; align-items: center; gap: 3px; font-size: 5.4px; font-weight: 600; color: var(--ink); white-space: nowrap; }
  .partner-dot { width: 8px; height: 8px; border-radius: 50%; border: 1.2px solid var(--ink); }

  .service-list { position: absolute; left: 5px; top: 17px; list-style: none; font-size: 5.6px; line-height: 7.8px; color: var(--ink-soft); }
  .service-list li { border-left: 0.7px solid var(--ink-soft); padding-left: 2px; }
  .service-list .cont { border-left-color: transparent; }
</style>
</head>
<body>
<svg width="0" height="0" style="position:absolute">
  <defs>
    <symbol id="icon-phone" viewBox="0 0 10 10"><path d="M2 0.5 L3.6 0.5 L4.2 3 L3 3.8 C3.6 5.4 4.6 6.4 6.2 7 L7 5.8 L9.5 6.4 L9.5 8 C9.5 9 8.8 9.5 8 9.5 C4 9.2 0.8 6 0.5 2 C0.5 1.2 1 0.5 2 0.5 Z"/></symbol>
    <symbol id="icon-mail" viewBox="0 0 10 10"><path d="M0.5 2 H9.5 V8 H0.5 Z M1.2 2.6 L5 5.6 L8.8 2.6" stroke="#2a2d30" stroke-width="0.8"/></symbol>
    <symbol id="icon-web" viewBox="0 0 10 10"><circle cx="5" cy="5" r="4.3"/><path d="M0.7 5 H9.3 M5 0.7 V9.3 M2 2.4 Q5 4 8 2.4 M2 7.6 Q5 6 8 7.6" stroke="#2a2d30" stroke-width="0.6" fill="none"/></symbol>
  </defs>
</svg>

<!-- Row 1 -->
<div class="card col-front accent-gold" style="top:78px">
  <div class="brand brand-lg" style="top:56px"><span class="brand-dot"></span><span class="brand-name">Seelenraum</span></div>
  <p class="services-line">Psycho-Kinesiologie nach Dr. Sonnfeld &nbsp;|&nbsp; Neurobiologie<br>Mentalfeldtherapie &nbsp;|&nbsp; Geistiges Familienstellen</p>
  <div class="motto">Gesundheit - Glück - Liebe - Frieden</div>
</div>
<div class="card col-back" style="top:78px">
  <div class="brand brand-sm" style="left:6px;top:20px"><span class="brand-dot"></span><span class="brand-name">Seelenraum</span></div>
  <div class="person" style="top:61px"><p class="person-name">Udo Brenner</p><p class="person-role">Systemanalytiker</p></div>
  <ul class="contacts" style="top:91px">
    <li><svg><use href="#icon-phone"/></svg>Schweiz</li><li class="indent">0041 790 000 412</li>
    <li><svg><use href="#icon-phone"/></svg>Deutschland</li><li class="indent">0049 170 000 58 36</li>
    <li><svg><use href="#icon-mail"/></svg>info@seelenraum-praxis.ch</li>
    <li><svg><use href="#icon-web"/></svg>www.seelenraum-praxis.ch</li>
  </ul>
  <div class="portrait" role="img" aria-label="Schwarz-Weiß-Porträtfoto des Therapeuten"></div>
  <div class="partner" style="left:165px;top:118px"><span class="partner-dot"></span>Lumen Harbor Circle</div>
  <div class="motto">Gesundheit - Glück - Liebe - Frieden</div>
</div>

<!-- Row 2 -->
<div class="card col-front dot-gold" style="top:251px">
  <div class="brand brand-lg" style="top:56px"><span class="brand-dot"></span><span class="brand-name">Seelenraum</span></div>
  <p class="services-line">Psycho-Kinesiologie nach Dr. Sonnfeld &nbsp;|&nbsp; Neurobiologie<br>Mentalfeldtherapie &nbsp;|&nbsp; Geistiges Familienstellen</p>
  <div class="motto">Gesundheit - Glück - Liebe - Frieden</div>
</div>
<div class="card col-back dot-gold" style="top:251px">
  <div class="brand brand-sm" style="left:6px;top:20px"><span class="brand-dot"></span><span class="brand-name">Seelenraum</span></div>
  <div class="person" style="top:61px"><p class="person-name">Udo Brenner</p><p class="person-role">Systemanalytiker</p></div>
  <ul class="contacts" style="top:91px">
    <li><svg><use href="#icon-phone"/></svg>Schweiz</li><li class="indent">0041 790 000 412</li>
    <li><svg><use href="#icon-phone"/></svg>Deutschland</li><li class="indent">0049 170 000 58 36</li>
    <li><svg><use href="#icon-mail"/></svg>info@seelenraum-praxis.ch</li>
    <li><svg><use href="#icon-web"/></svg>www.seelenraum-praxis.ch</li>
  </ul>
  <div class="portrait" role="img" aria-label="Schwarz-Weiß-Porträtfoto des Therapeuten"></div>
  <div class="partner" style="left:165px;top:118px"><span class="partner-dot"></span>Lumen Harbor Circle</div>
  <div class="motto">Gesundheit - Glück - Liebe - Frieden</div>
</div>

<!-- Row 3 -->
<div class="card col-front accent-gold" style="top:436px">
  <div class="brand brand-lg" style="top:60px"><span class="brand-dot"></span><span class="brand-name">Seelenraum</span></div>
  <p class="front-name">Udo Brenner</p>
  <div class="motto">Gesundheit - Glück - Liebe - Frieden</div>
</div>
<div class="card col-back" style="top:436px">
  <ul class="service-list"><li>Psycho-Kinesiologie</li><li class="cont">nach Dr. Sonnfeld</li><li>Neurobiologie</li><li>Mentalfeldtherapie</li><li>Geistiges Familienstellen</li></ul>
  <div class="brand brand-sm" style="left:120px;top:26px"><span class="brand-dot"></span><span class="brand-name">Seelenraum</span></div>
  <div class="person" style="left:120px;top:77px"><p class="person-name">Udo Brenner</p><p class="person-role">Systemanalytiker</p></div>
  <ul class="contacts" style="top:80px">
    <li><svg><use href="#icon-phone"/></svg>Schweiz</li><li class="indent">0041 790 000 412</li>
    <li class="gap"><svg><use href="#icon-phone"/></svg>Deutschland</li><li class="indent">0049 170 000 58 36</li>
    <li class="gap"><svg><use href="#icon-mail"/></svg>info@seelenraum-praxis.ch</li>
    <li class="gap"><svg><use href="#icon-web"/></svg>www.seelenraum-praxis.ch</li>
  </ul>
  <div class="partner" style="left:165px;top:117px"><span class="partner-dot"></span>Lumen Harbor Circle</div>
  <div class="motto">Gesundheit - Glück - Liebe - Frieden</div>
</div>

<!-- Row 4 -->
<div class="card col-front dot-gold" style="top:608px">
  <div class="brand brand-lg" style="top:60px"><span class="brand-dot"></span><span class="brand-name">Seelenraum</span></div>
  <p class="front-name">Udo Brenner</p>
  <div class="motto">Gesundheit - Glück - Liebe - Frieden</div>
</div>
<div class="card col-back dot-gold" style="top:608px">
  <ul class="service-list"><li>Psycho-Kinesiologie</li><li class="cont">nach Dr. Sonnfeld</li><li>Neurobiologie</li><li>Mentalfeldtherapie</li><li>Geistiges Familienstellen</li></ul>
  <div class="brand brand-sm" style="left:120px;top:26px"><span class="brand-dot"></span><span class="brand-name">Seelenraum</span></div>
  <div class="person" style="left:120px;top:77px"><p class="person-name">Udo Brenner</p><p class="person-role">Systemanalytiker</p></div>
  <ul class="contacts" style="top:80px">
    <li><svg><use href="#icon-phone"/></svg>Schweiz</li><li class="indent">0041 790 000 412</li>
    <li class="gap"><svg><use href="#icon-phone"/></svg>Deutschland</li><li class="indent">0049 170 000 58 36</li>
    <li class="gap"><svg><use href="#icon-mail"/></svg>info@seelenraum-praxis.ch</li>
    <li class="gap"><svg><use href="#icon-web"/></svg>www.seelenraum-praxis.ch</li>
  </ul>
  <div class="partner" style="left:165px;top:117px"><span class="partner-dot"></span>Lumen Harbor Circle</div>
  <div class="motto">Gesundheit - Glück - Liebe - Frieden</div>
</div>

<!-- Row 5 -->
<div class="card col-front dot-gold" style="top:785px">
  <div class="brand brand-lg" style="top:60px"><span class="brand-dot"></span><span class="brand-name">Seelenraum</span></div>
  <p class="front-name">Udo Brenner</p>
  <div class="motto">Gesundheit - Glück - Liebe - Frieden</div>
</div>
<div class="card col-back dot-gold" style="top:785px">
  <ul class="service-list"><li>Psycho-Kinesiologie</li><li class="cont">nach Dr. Sonnfeld</li><li>Neurobiologie</li><li>Mentalfeldtherapie</li><li>Geistiges Familienstellen</li></ul>
  <div class="brand brand-sm" style="left:120px;top:26px"><span class="brand-dot"></span><span class="brand-name">Seelenraum</span></div>
  <div class="person" style="left:120px;top:77px"><p class="person-name">Udo Brenner</p><p class="person-role">Systemanalytiker</p></div>
  <ul class="contacts" style="top:80px">
    <li><svg><use href="#icon-phone"/></svg>Schweiz</li><li class="indent">0041 790 000 412</li>
    <li class="gap"><svg><use href="#icon-phone"/></svg>Deutschland</li><li class="indent">0049 170 000 58 36</li>
    <li class="gap"><svg><use href="#icon-mail"/></svg>info@seelenraum-praxis.ch</li>
    <li class="gap"><svg><use href="#icon-web"/></svg>www.seelenraum-praxis.ch</li>
  </ul>
  <div class="partner" style="left:165px;top:117px"><span class="partner-dot"></span>Lumen Harbor Circle</div>
  <div class="motto">Gesundheit - Glück - Liebe - Frieden</div>
</div>

<!-- Row 6 -->
<div class="card col-front dot-grey tone-grey" style="top:958px">
  <div class="brand brand-lg" style="top:60px"><span class="brand-dot"></span><span class="brand-name">Seelenraum</span></div>
  <p class="front-name">Udo Brenner</p>
  <div class="motto">Gesundheit - Glück - Liebe - Frieden</div>
</div>
<div class="card col-back dot-grey tone-grey" style="top:958px">
  <ul class="service-list"><li>Psycho-Kinesiologie</li><li class="cont">nach Dr. Sonnfeld</li><li>Neurobiologie</li><li>Mentalfeldtherapie</li><li>Geistiges Familienstellen</li></ul>
  <div class="brand brand-sm" style="left:120px;top:26px"><span class="brand-dot"></span><span class="brand-name">Seelenraum</span></div>
  <div class="person" style="left:120px;top:77px"><p class="person-name">Udo Brenner</p><p class="person-role">Systemanalytiker</p></div>
  <ul class="contacts" style="top:80px">
    <li><svg><use href="#icon-phone"/></svg>Schweiz</li><li class="indent">0041 790 000 412</li>
    <li class="gap"><svg><use href="#icon-phone"/></svg>Deutschland</li><li class="indent">0049 170 000 58 36</li>
    <li class="gap"><svg><use href="#icon-mail"/></svg>info@seelenraum-praxis.ch</li>
    <li class="gap"><svg><use href="#icon-web"/></svg>www.seelenraum-praxis.ch</li>
  </ul>
  <div class="partner" style="left:165px;top:117px"><span class="partner-dot"></span>Lumen Harbor Circle</div>
  <div class="motto">Gesundheit - Glück - Liebe - Frieden</div>
</div>
</body>
</html>
```